Alcohol Marketing website

Home page and information page design, details as follows

CLIENT PURPOSE
Increase online visibility and create good contacts to increase business.

SERVICES
Drinks Marketing Consultancy
Brand Representation
Spirit Brand Sales & Marketing
Brand Development
Brand Distribution
Brand Launch & Introductions

COMPETITION
hazelpour.co.uk -
quintaloft.co.uk -

WEBSITE(S) CLIENT LIKES
Small competitors I admire:
http://www.hazelpour.co.uk/main.htm
http://www.quintaloft.com
http://www.morvatide.co.uk/spiritsliqueursbybrand.php
http://www.kelbrowhouse.com/page1.html
http://www.quorrifenwave.co.uk/index.asp

Nice page layout:
http://www.nkplume.com/
http://www.wzoharbour.com/
http://www.pelvit.com/index.cfm?do=pelvit.home

WEBSITE CLIENT DOES NOT LIKE
http://www.corvanhall.com/
http://www.amberlode-hall.com/
http://www.thesupperfold.co.uk/aboutUs.html
http://www.grainandkettle.com/
http://www.tessmarrow.co.uk/default.asp
http://www.pinnock-halden.co.uk/start.htm
http://www.rilby.co.uk/
http://www.vmkettles.com/default2.aspx
http://www.tumbril-vale.co.uk/mainpage.aspx

COMPANY LOGO
Customer has a company logo (Supplied)

COLOURS:
Blue
White

STRAPLINE:
No

WEBSITE THEME: Marketing

IMAGES THAT BEST REFLECT THE COMPANY:
Spirits / Drinks

HEADER IMAGE:
Spirits / Brands

PAGES:
home
strength& flavour
a little about us
our spirit marketing
big brand success
speak to us

USER JOURNEYS:
General Service > Land on website >Navigation > Info Pages > Contact Form
Questions > Land on website > Message Banners > Info Pages > Contact Form
Contact > Land on website > Clear Telephone / Email Banner > Contact Form

CALL TO ACTION BANNER:
If you need help making your drink the next big brand, speak to us today.

KEYWORDS THAT RELATE TO THE BUSINESS:
brand marketing
drinks marketing
spirits marketing
brand marketing strategy
alcoholic drinks marketing
Drinks Brand Development

LOCATION(S):
United Kingdom -
Worldwide -

Target Market(s)

Male & Female
30-60
Marketing Directors
Brand Developers
Export Directors
Brand Managers

Industry/Entity Type

Marketing

Number of Pages Required

2 pages

Requirements
Must have
• This design will be integrated into wordpress, I have attached a wireframe of what we need, this is NOT a strict guide but contains content that is essential, the wireframes shows the priority of statements and products. the images supplied need to sell the products and services.
The main banner will eventually be animated so this needs to be taken into account.
The cliemt has supplied images which will need to be used in the design , however if you feel you have better images in the same style then they can be used.
Nice to have
• animation included, Jquery
Should not have
• NO fully flash sites or designs, this site will be Search engine optimised and updateable

```html
<!DOCTYPE html>
<html lang="en">
<head>
<meta charset="utf-8">
<title>Proof &amp; Palate – Drinks Brand Marketing</title>
<link href="https://fonts.googleapis.com/css2?family=Ubuntu:ital,wght@0,400;0,500;1,300;1,400;1,500&display=swap" rel="stylesheet">
<style>
  :root{
    --bg-deep:#08121b;
    --bg-mid:#1d3448;
    --frame-white:#ffffff;
    --ink:#0d0d0d;
    --bar-dark:#111111;
    --accent:#1aa3e3;
    --accent-soft:#5bbbe9;
    --nav-top:#ffffff;
    --nav-bottom:#d3e9f6;
    --text-light:#ffffff;
    --muted:#9a9a9a;
  }
  *{margin:0;padding:0;box-sizing:border-box}
  html,body{width:1200px;height:971px;overflow:hidden}
  body{
    background:radial-gradient(ellipse at 50% 40%,var(--bg-mid) 0%,#14273a 45%,var(--bg-deep) 100%);
    font-family:"Ubuntu",sans-serif;
    position:relative;
  }
  .site-frame{
    position:absolute;left:103px;top:98px;width:993px;height:814px;
    background:var(--bar-dark);
    border:3px solid var(--frame-white);
    border-radius:20px;
    overflow:hidden;
  }
  .top-bar{
    position:absolute;left:0;top:0;width:100%;height:38px;
    background:var(--bar-dark);
    color:var(--text-light);font-size:13px;font-weight:500;white-space:nowrap;
  }
  .social-links{position:absolute;left:12px;top:9px;display:flex;gap:10px}
  .social-links span{display:flex;align-items:center;gap:6px}
  .social-links i{display:inline-block;width:18px;height:18px;background:var(--accent);border-radius:3px}
  .contact-line{position:absolute;right:12px;top:10px;display:flex;gap:6px;align-items:center}
  .contact-line b{color:var(--accent);font-weight:500}
  .main-nav{
    position:absolute;left:0;top:38px;width:100%;height:68px;
    background:linear-gradient(var(--nav-top),var(--nav-bottom));
    font-size:17px;font-weight:500;color:var(--ink);
    line-height:1.02;text-align:center;white-space:nowrap;
  }
  .main-nav span{position:absolute;top:13px}
  .hero{
    position:absolute;left:0;top:109px;width:100%;height:438px;
  }
  .hero-photo{
    position:absolute;inset:0;
    background:
      radial-gradient(ellipse at 68% 42%,rgba(225,230,235,.75) 0%,rgba(120,130,150,.35) 14%,transparent 30%),
      radial-gradient(ellipse at 70% 75%,rgba(40,60,190,.55) 0%,transparent 18%),
      radial-gradient(ellipse at 75% 85%,#6a3a2a 0%,transparent 45%),
      linear-gradient(100deg,#050505 0%,#0b0b0b 35%,#2a1a14 60%,#3a2418 80%,#1a2a2a 100%);
  }
  .open-mark{
    position:absolute;left:18px;top:18px;
    color:var(--text-light);font-style:italic;font-weight:300;font-size:80px;line-height:80px;
  }
  .hero-quote{
    position:absolute;left:40px;top:56px;
    color:var(--text-light);font-style:italic;font-weight:300;
    font-size:75px;line-height:77px;letter-spacing:.5px;white-space:nowrap;
  }
  .hero-quote strong{font-weight:500}
  .hero-quote .close-mark{display:inline-block;font-size:80px;line-height:40px;vertical-align:top;margin-top:8px}
  .quote-credit{
    position:absolute;left:256px;top:338px;
    color:var(--accent-soft);font-style:italic;font-size:16px;line-height:21px;
  }
  .quote-credit em{font-weight:500}
  .feature-row{
    position:absolute;left:0;top:550px;width:100%;height:217px;
    display:flex;gap:3px;background:var(--frame-white);
  }
  .feature-card{position:relative;flex:1;overflow:hidden}
  .feature-card .card-photo{position:absolute;inset:0}
  .card-a .card-photo{background:radial-gradient(ellipse at 78% 55%,#e6a42a 0%,#8a4a10 25%,transparent 55%),linear-gradient(#1a1a1a,#3a2a1a)}
  .card-b .card-photo{background:radial-gradient(ellipse at 45% 80%,#c8d24a 0%,#5a5a20 18%,transparent 40%),radial-gradient(ellipse at 15% 90%,#d08a3a 0%,transparent 25%),linear-gradient(#151515,#2a2018)}
  .card-c .card-photo{background:radial-gradient(ellipse at 70% 70%,#5a6a78 0%,transparent 45%),linear-gradient(#0d1418,#2a2e30)}
  .card-body{position:absolute;left:18px;top:15px;right:4px;color:var(--text-light)}
  .card-body h2{
    font-size:28px;font-weight:400;line-height:28px;position:relative;margin-bottom:8px;white-space:nowrap;
  }
  .card-body h2::before{
    content:"";position:absolute;left:-19px;top:6px;
    border-left:10px solid var(--accent);border-top:8px solid transparent;border-bottom:8px solid transparent;
  }
  .card-body p{font-family:Arial,sans-serif;font-size:11px;line-height:15px}
  .read-more{
    display:inline-block;margin-top:5px;background:var(--accent);color:var(--text-light);
    font-family:Arial,sans-serif;font-size:11px;font-weight:bold;padding:2px 4px;
  }
  .keyword-bar{
    position:absolute;left:3px;top:773px;width:981px;height:36px;
    border:2px solid #555;border-radius:6px;background:var(--bar-dark);
    display:flex;justify-content:center;align-items:center;gap:11px;
    font-family:Arial,sans-serif;color:var(--text-light);font-size:13px;white-space:nowrap;
  }
  .keyword-bar .sep{color:var(--accent);font-size:14px}
  .brand-box{
    position:absolute;left:414px;top:51px;width:372px;height:180px;
    background:var(--bar-dark);border:3px solid var(--frame-white);border-radius:18px;padding:7px;
  }
  .brand-inner{
    width:100%;height:100%;border-radius:10px;
    background:linear-gradient(#ffffff 35%,#cfe8f7);
    display:flex;justify-content:center;align-items:flex-start;gap:10px;padding-top:22px;
  }
  .brand-name{font-size:29px;font-weight:500;color:var(--ink);letter-spacing:.3px}
  .brand-dot{width:16px;height:16px;border-radius:50%;background:var(--accent);margin-top:10px}
  .legal-tab{
    position:absolute;left:416px;top:912px;width:367px;height:26px;
    background:var(--bar-dark);border-radius:0 0 14px 14px;
    color:var(--muted);font-family:Arial,sans-serif;font-size:11px;
    display:flex;justify-content:center;align-items:center;gap:7px;
  }
</style>
</head>
<body>
  <div class="site-frame">
    <div class="top-bar">
      <div class="social-links">
        <span><i></i>follow on our page</span>
        <span><i></i>follow on our feed</span>
      </div>
      <div class="contact-line">020 7946 0381 <b>✱</b> info@proofandpalate.com</div>
    </div>

    <nav class="main-nav">
      <span style="left:14px">proof<br>&amp; palate</span>
      <span style="left:104px">a little bit<br>about us</span>
      <span style="left:205px">our spirit<br>marketing</span>
      <span style="left:700px">big brand<br>success</span>
      <span style="left:801px;top:24px">our blog</span>
      <span style="left:891px;top:24px">speak to us</span>
    </nav>

    <section class="hero">
      <div class="hero-photo" role="img" aria-label="Cocktail in a martini glass with blue stem on a bar counter"></div>
      <span class="open-mark">“</span>
      <p class="hero-quote">turning our<br>small time whiskey<br>into <strong>a national</strong><br>brand <span class="close-mark">“</span></p>
      <p class="quote-credit">Dan Whitlow<br><em>Corvane</em></p>
    </section>

    <section class="feature-row">
      <article class="feature-card card-a">
        <div class="card-photo" role="img" aria-label="Glowing amber spirit bottle with bubbles"></div>
        <div class="card-body">
          <h2>22 years experience<br>with big brands</h2>
          <p>Lorem ipsum dolor sit amet, consectetur adipiscing elit.<br>Curabitur fringilla, diam eget vehicula eleifend, dui nisl tempus<br>nunc, vel pharetra metus mauris ultrices diam.</p>
          <span class="read-more">READ MORE</span>
        </div>
      </article>
      <article class="feature-card card-b">
        <div class="card-photo" role="img" aria-label="Green cocktail beside a candle on a bar"></div>
        <div class="card-body">
          <h2>Making your drink<br>the next BIG brand</h2>
          <p>Lorem ipsum dolor sit amet, consectetur adipiscing elit.<br>Curabitur fringilla, diam eget vehicula eleifend, dui nisl tempus<br>nunc, vel pharetra metus mauris ultrices diam.</p>
          <span class="read-more">READ MORE</span>
        </div>
      </article>
      <article class="feature-card card-c">
        <div class="card-photo" role="img" aria-label="Back bar shelves lined with spirit bottles and glasses"></div>
        <div class="card-body">
          <h2>350 Outlets that<br>listen to what we say</h2>
          <p>Lorem ipsum dolor sit amet, consectetur adipiscing elit.<br>Curabitur fringilla, diam eget vehicula eleifend, dui nisl tempus<br>nunc, vel pharetra metus mauris ultrices diam.</p>
          <span class="read-more">READ MORE</span>
        </div>
      </article>
    </section>

    <footer class="keyword-bar">
      <span>Brand Marketing</span><span class="sep">✱</span>
      <span>Brand Marketing Strategy</span><span class="sep">✱</span>
      <span>Drinks Marketing</span><span class="sep">✱</span>
      <span>Spirits Marketing</span><span class="sep">✱</span>
      <span>Alcoholic Drinks Marketing</span><span class="sep">✱</span>
      <span>Drinks Brand Development</span>
    </footer>
  </div>

  <div class="brand-box">
    <div class="brand-inner">
      <span class="brand-name">PROOF &amp; PALATE</span>
      <span class="brand-dot"></span>
    </div>
  </div>

  <div class="legal-tab">
    <span>©2010 Proof &amp; Palate</span><span>|</span><span>Terms &amp; Conditions</span><span>|</span><span>Privacy Policy</span>
  </div>
</body>
</html>
```